Popup Banners - BrightCounsel - Legal Technology

- We need two banners (same style) designed with two different images and different text.

- The details of the printing requirements are attached, along with suggested images.

- The banners should share the same theme as our website www.brightcounsel.com.au

- The first banner would include our logo (attached), use the 'roads join' image (attached) in some way and text: New Opportunities - Where legal services and technology meet.

- The second banner would include our logo (attached), use the 'jigsaw' image (attached) in some way and use text: Legal Technology Strategy, Advice and Capability.

- Details on what are required from the Printer is attached also.

Target Market(s)

Legal Professionals

Industry/Entity Type

Information Technology

Font styles to use
Sans Serif

Requirements
Must have
• Our logo (attached), suggested text and the image mentioned for each.
Nice to have
• Professional and modern look
Should not have
• Cheap looking

```html
<!DOCTYPE html>
<html lang="en">
<head>
<meta charset="utf-8">
<title>BrightCounsel – Popup Banners</title>
<link rel="stylesheet" href="https://fonts.googleapis.com/css2?family=Ubuntu:wght@300;400;700&family=Caveat+Brush&display=swap">
<style>
  :root {
    --page: #ffffff;
    --navy: #0c2237;
    --steel: #6a6d7d;
    --accent-blue: #1a5fae;
    --orange: #f07a3a;
    --white: #ffffff;
  }
  html, body {
    margin: 0;
    padding: 0;
    width: 1200px;
    height: 1200px;
    overflow: hidden;
    background: var(--page);
  }
  .canvas {
    position: relative;
    width: 1200px;
    height: 1200px;
    font-family: "Ubuntu", sans-serif;
  }
  .banner {
    position: absolute;
    width: 362px;
    height: 889px;
    display: block;
  }
  .banner--strategy { left: 182px; top: 46px; }
  .banner--opportunities { left: 657px; top: 264px; }

  .fill-navy { fill: var(--navy); }
  .fill-steel { fill: var(--steel); }
  .rule { stroke: var(--white); stroke-width: 2.2; }

  .brand-name {
    font-family: "Ubuntu", sans-serif;
    font-weight: 400;
    font-size: 24px;
    letter-spacing: 4px;
    fill: var(--white);
  }
  .headline {
    font-family: "Ubuntu", sans-serif;
    font-weight: 700;
    fill: var(--white);
  }
  .ampersand {
    font-family: "Ubuntu", sans-serif;
    font-weight: 700;
    font-size: 110px;
    fill: var(--accent-blue);
  }
  .service-label {
    font-family: "Ubuntu", sans-serif;
    font-weight: 300;
    font-size: 15px;
    fill: var(--white);
  }
  .script-word {
    font-family: "Caveat Brush", cursive;
    font-size: 64px;
    fill: var(--orange);
  }
  .tagline {
    font-family: "Ubuntu", sans-serif;
    font-weight: 300;
    font-size: 27px;
    fill: var(--white);
  }
  .icon-ring { fill: none; stroke: var(--white); stroke-width: 1.6; }
  .icon-line {
    fill: none;
    stroke: var(--white);
    stroke-width: 1.3;
    stroke-linecap: round;
    stroke-linejoin: round;
  }
  .cycle-ring { fill: none; stroke: var(--white); stroke-width: 2.6; }
  .cycle-arrow { fill: none; stroke: var(--white); stroke-width: 2.2; }
</style>
</head>
<body>
<div class="canvas">

  <svg width="0" height="0" style="position:absolute" aria-hidden="true">
    <defs>
      <symbol id="icon-flag" viewBox="-10 -10 20 20">
        <path class="icon-line" d="M-5 8 V-7 M-5 -6 C-2 -8 1 -4 5 -6 V1 C1 3 -2 -1 -5 1"/>
      </symbol>
      <symbol id="icon-chart" viewBox="-10 -10 20 20">
        <rect class="icon-line" x="-7" y="-7" width="14" height="10"/>
        <path class="icon-line" d="M0 3 L-3 8 M0 3 L3 8 M0 3 V8 M-5 1 L-2 -3 L1 -1 L5 -5"/>
      </symbol>
      <symbol id="icon-puzzle" viewBox="-10 -10 20 20">
        <path class="icon-line" d="M-6 -3 H-2 V-5 A2 2 0 1 1 2 -5 V-3 H6 V7 H-6 V4 H-4 A2 2 0 1 0 -4 0 H-6 Z"/>
      </symbol>
      <symbol id="icon-cart" viewBox="-10 -10 20 20">
        <path class="icon-line" d="M-8 -6 H-5 L-3 4 H6 L7 -3 H-4"/>
        <circle class="icon-line" cx="-2" cy="7" r="1.2"/>
        <circle class="icon-line" cx="5" cy="7" r="1.2"/>
      </symbol>
      <marker id="arrow-head" viewBox="0 0 10 10" refX="8" refY="5" markerWidth="5" markerHeight="5" orient="auto">
        <path d="M0 0 L10 5 L0 10 Z" fill="#ffffff"/>
      </marker>
      <radialGradient id="jigsaw-glow" cx="0.55" cy="0.5" r="0.65">
        <stop offset="0" stop-color="#cfe3f5"/>
        <stop offset="0.25" stop-color="#5b8fbf"/>
        <stop offset="0.7" stop-color="#1d4a73"/>
        <stop offset="1" stop-color="#0c2740"/>
      </radialGradient>
      <linearGradient id="sky-fade" x1="0" y1="0" x2="0" y2="1">
        <stop offset="0" stop-color="#1778c2"/>
        <stop offset="0.6" stop-color="#2a8bd0"/>
        <stop offset="1" stop-color="#3f97d6"/>
      </linearGradient>
      <linearGradient id="roads-scene" x1="0" y1="0" x2="0" y2="1">
        <stop offset="0" stop-color="#3f97d6"/>
        <stop offset="0.1" stop-color="#8fbfe0"/>
        <stop offset="0.16" stop-color="#6f9a48"/>
        <stop offset="0.6" stop-color="#5c8f36"/>
        <stop offset="1" stop-color="#4c7d2c"/>
      </linearGradient>
    </defs>
  </svg>

  <!-- Banner: Legal Technology Strategy -->
  <svg class="banner banner--strategy" viewBox="0 0 362 889" role="group" aria-label="BrightCounsel banner: Legal Technology Strategy, Advice and Capability">
    <rect class="fill-navy" x="0" y="0" width="362" height="889"/>

    <g class="brand">
      <text class="brand-name" x="328" y="72" text-anchor="end">BrightCounsel</text>
      <line class="rule" x1="34" y1="87" x2="328" y2="87"/>
    </g>

    <g class="headline-block">
      <text class="headline" x="303" y="144" font-size="42" text-anchor="end" textLength="118" lengthAdjust="spacingAndGlyphs">LEGAL</text>
      <text class="headline" x="91" y="166" font-size="20" textLength="240" lengthAdjust="spacingAndGlyphs">TECHNOLOGY STRATEGY</text>
      <text class="ampersand" x="256" y="256" textLength="76" lengthAdjust="spacingAndGlyphs">&amp;</text>
      <text class="headline" x="247" y="210" font-size="42" text-anchor="end" textLength="142" lengthAdjust="spacingAndGlyphs">ADVICE</text>
      <text class="headline" x="38" y="252" font-size="42" textLength="228" lengthAdjust="spacingAndGlyphs">CAPABILITY</text>
    </g>

    <g class="service-list">
      <rect class="fill-steel" x="0" y="276" width="362" height="41"/>
      <circle class="icon-ring" cx="60" cy="296" r="16"/>
      <use href="#icon-flag" x="49" y="285" width="22" height="22"/>
      <text class="service-label" x="84" y="301">ESTABLISHED</text>

      <rect class="fill-steel" x="0" y="332" width="362" height="41"/>
      <circle class="icon-ring" cx="301" cy="352" r="16"/>
      <use href="#icon-chart" x="290" y="341" width="22" height="22"/>
      <text class="service-label" x="276" y="357" text-anchor="end">PROCESS AUTOMATION</text>

      <rect class="fill-steel" x="0" y="388" width="362" height="41"/>
      <circle class="icon-ring" cx="60" cy="408" r="16"/>
      <use href="#icon-puzzle" x="49" y="397" width="22" height="22"/>
      <text class="service-label" x="84" y="413">STRATEGIC REVIEW</text>

      <rect class="fill-steel" x="0" y="444" width="362" height="41"/>
      <circle class="icon-ring" cx="301" cy="464" r="16"/>
      <use href="#icon-cart" x="290" y="453" width="22" height="22"/>
      <text class="service-label" x="276" y="469" text-anchor="end">INDUSTRY RESEARCH</text>
    </g>

    <line class="rule" x1="0" y1="500" x2="362" y2="500" stroke-width="1.6"/>
    <rect x="0" y="502" width="362" height="387" fill="url(#jigsaw-glow)" role="img" aria-label="Photo: a hand placing a glowing jigsaw piece into a blue puzzle"/>
  </svg>

  <!-- Banner: New Opportunities -->
  <svg class="banner banner--opportunities" viewBox="0 0 362 889" role="group" aria-label="BrightCounsel banner: New Opportunities, where legal services and technology meet">
    <rect x="0" y="0" width="362" height="889" fill="url(#sky-fade)"/>

    <g class="brand">
      <text class="brand-name" x="329" y="90" text-anchor="end">BrightCounsel</text>
      <line class="rule" x1="33" y1="107" x2="329" y2="107"/>
    </g>

    <g class="headline-block">
      <text class="script-word" x="35" y="203" textLength="145" lengthAdjust="spacingAndGlyphs">NEW</text>
      <text class="headline" x="46" y="234" font-size="42" textLength="282" lengthAdjust="spacingAndGlyphs">OPPORTUNITIES</text>
      <text class="tagline" x="181" y="292" text-anchor="middle" textLength="310" lengthAdjust="spacingAndGlyphs">WHERE LEGAL SERVICES &amp;</text>
      <text class="tagline" x="181" y="324" text-anchor="middle" textLength="236" lengthAdjust="spacingAndGlyphs">TECHNOLOGY MEET</text>
    </g>

    <g class="service-cycle">
      <circle class="cycle-ring" cx="181" cy="388" r="28"/>
      <use href="#icon-flag" x="164" y="371" width="34" height="34"/>
      <circle class="cycle-ring" cx="264" cy="473" r="28"/>
      <use href="#icon-chart" x="247" y="456" width="34" height="34"/>
      <circle class="cycle-ring" cx="181" cy="558" r="28"/>
      <use href="#icon-puzzle" x="164" y="541" width="34" height="34"/>
      <circle class="cycle-ring" cx="96" cy="473" r="28"/>
      <use href="#icon-cart" x="79" y="456" width="34" height="34"/>

      <path class="cycle-arrow" d="M221 398 A 60 60 0 0 1 257 438" marker-end="url(#arrow-head)"/>
      <path class="cycle-arrow" d="M257 510 A 60 60 0 0 1 221 549" marker-end="url(#arrow-head)"/>
      <path class="cycle-arrow" d="M140 548 A 60 60 0 0 1 104 509" marker-end="url(#arrow-head)"/>
      <path class="cycle-arrow" d="M105 437 A 60 60 0 0 1 142 397" marker-end="url(#arrow-head)"/>
    </g>

    <rect x="0" y="595" width="362" height="294" fill="url(#roads-scene)" role="img" aria-label="Photo: two dirt roads joining on a green grassy hill under a blue sky"/>
  </svg>

</div>
</body>
</html>
```